Quote Cards for Social Media RV

I would like to put these quotes over one of the pictures attached; One Quote per picture, and I want the quote to be bold or easy to read as well. I provided a few reference graphics that I really like as examples below. In very small letters at the bottom add @RVCarloweDaily

All of the pictures are attached; you can pick any photo and add one quote to it; but no stock photography

Target Market(s)

women trying to lose weight

Requirements
Must have
• quotes and pictures attached
Should not have
• no stock photography

```html
<!DOCTYPE html>
<html lang="en">
<head>
<meta charset="utf-8">
<title>Quote Card</title>
<link href="https://fonts.googleapis.com/css2?family=Oswald:wght@600&family=Montserrat:wght@600&display=swap" rel="stylesheet">
<style>
:root{
  --wall-light:#e6dccd;
  --wall-mid:#d8cbb8;
  --sweater:#b08862;
  --text-light:#ffffff;
  --frame-line:rgba(255,255,255,0.75);
}
html,body{margin:0;padding:0;overflow:hidden;}
body{width:1107px;height:1200px;}
.quote-card{
  position:relative;width:1107px;height:1200px;overflow:hidden;
  background:var(--wall-light);
}
.portrait-photo{
  position:absolute;inset:0;
  background:
    radial-gradient(ellipse 34% 52% at 52% 62%, var(--sweater) 0%, rgba(176,136,98,0.85) 55%, rgba(176,136,98,0) 100%),
    linear-gradient(90deg, var(--wall-mid), var(--wall-light) 40%, var(--wall-light) 70%, var(--wall-mid));
}
.bottom-shade{
  position:absolute;left:0;right:0;bottom:0;height:560px;
  background:linear-gradient(180deg, rgba(58,51,45,0) 0%, rgba(58,51,45,0.45) 45%, rgba(40,35,31,0.85) 100%);
}
.inner-frame{
  position:absolute;left:35px;top:29px;width:1045px;height:1138px;
  border:1.5px solid var(--frame-line);box-sizing:border-box;
}
.quote-text{
  position:absolute;left:95px;top:764px;margin:0;
  font-family:'Oswald',sans-serif;font-weight:600;font-size:78px;
  line-height:81px;letter-spacing:0.5px;text-transform:uppercase;
  color:var(--text-light);
}
.quote-line{
  display:block;white-space:nowrap;
  transform:scaleX(0.86);transform-origin:left center;
}
.handle{
  position:absolute;left:95px;top:1053px;margin:0;
  font-family:'Montserrat',sans-serif;font-weight:600;font-size:30px;
  letter-spacing:2px;white-space:nowrap;color:var(--text-light);
}
</style>
</head>
<body>
<div class="quote-card">
  <div class="portrait-photo" role="img" aria-label="Smiling woman in a camel ribbed turtleneck and black jeans, hand on hip, standing before a pale stone wall"></div>
  <div class="bottom-shade"></div>
  <div class="inner-frame"></div>
  <p class="quote-text">
    <span class="quote-line">Finally-a natural solution</span>
    <span class="quote-line">that flattens your belly</span>
    <span class="quote-line">and eases stomach bloat</span>
  </p>
  <p class="handle">@RVCarloweDaily</p>
</div>
</body>
</html>
```